TIDAL VERGE needs bisness cards pronto

Bisness name is "TIDAL VERGE" new bisness the bisness includes lawn mowing, garden matanace, and any jobs around the house.
I need a card that is colorful and vibrant and the bisness of lawn mowing maybe with some nature with it. It also needs my contact details"Darren Quellby mobile 0413562049 call for free quote and email norma.vance@fernmail.com.au and a catchy tag line

Industry/Entity Type

House

Requirements
Must have
• Bisness name "TIDAL VERGE"
Contact details "0413562049"
Email norma.vance@fernmail.com.au
Call for free quote

```html
<!DOCTYPE html>
<html lang="en">
<head>
<meta charset="utf-8">
<title>Tidal Verge – Business Cards</title>
<link rel="stylesheet" href="https://fonts.googleapis.com/css2?family=Questrial&family=Lobster+Two:ital,wght@1,400;1,700&display=swap">
<style>
  :root {
    --canvas: #ffffff;
    --card-dark: #000000;
    --card-light: #ffffff;
    --leaf: #8dba1a;
    --ink-light: #ffffff;
    --ink-dark: #111111;
    --card-border: #111111;
  }
  * { margin: 0; padding: 0; box-sizing: border-box; }
  html, body {
    width: 1200px; height: 1000px; overflow: hidden;
    background: var(--canvas);
  }
  .sheet { position: relative; width: 1200px; height: 1000px; }

  .card {
    position: absolute; width: 515px; height: 286px;
    overflow: hidden;
  }
  .card--dark { background: var(--card-dark); color: var(--ink-light); }
  .card--light { background: var(--card-light); color: var(--ink-dark); border: 2px solid var(--card-border); }

  .card--front-top { left: 73px; top: 150px; }
  .card--back-top { left: 613px; top: 150px; }
  .card--front-bottom { left: 73px; top: 565px; }
  .card--back-bottom { left: 613px; top: 565px; }

  .brand { position: absolute; text-align: center; }
  .brand__name {
    font-family: "Questrial", sans-serif;
    color: var(--leaf);
    letter-spacing: 2px;
    white-space: nowrap;
    line-height: 1;
  }
  .brand__tagline {
    font-family: "Lobster Two", cursive;
    font-style: italic;
    margin-top: 8px;
    white-space: nowrap;
  }
  .card--dark .brand__tagline { color: var(--ink-light); }
  .card--light .brand__tagline { color: var(--ink-dark); }

  .brand--front { left: 0; right: 0; top: 120px; }
  .brand--front .brand__name { font-size: 40px; }
  .brand--front .brand__tagline { font-size: 15px; }

  .brand--back { left: 260px; width: 230px; top: 52px; }
  .brand--back .brand__name { font-size: 26px; }
  .brand--back .brand__tagline { font-size: 12px; margin-top: 6px; }

  .contact {
    position: absolute; left: 31px; top: 156px;
    font-family: "Questrial", sans-serif;
  }
  .contact__person { font-size: 18px; margin-bottom: 12px; }
  .contact__line { font-size: 16px; line-height: 19px; display: flex; }
  .contact__label { color: var(--leaf); width: 31px; }
  .contact__cta {
    margin-top: 12px;
    font-family: "Lobster Two", cursive;
    font-style: italic; font-weight: 700;
    font-size: 18px; color: var(--leaf);
  }
</style>
</head>
<body>
<main class="sheet">

  <section class="card card--dark card--front-top">
    <div class="brand brand--front">
      <div class="brand__name">TIDAL VERGE</div>
      <div class="brand__tagline">We'll take care of it.</div>
    </div>
  </section>

  <section class="card card--dark card--back-top">
    <div class="brand brand--back">
      <div class="brand__name">TIDAL VERGE</div>
      <div class="brand__tagline">We'll take care of it.</div>
    </div>
    <div class="contact">
      <div class="contact__person">Darren Quellby</div>
      <div class="contact__line"><span class="contact__label">m:</span><span>0413562049</span></div>
      <div class="contact__line"><span class="contact__label">e:</span><span>norma.vance@fernmail.com.au</span></div>
      <div class="contact__cta">Call for free quote</div>
    </div>
  </section>

  <section class="card card--dark card--front-bottom">
    <div class="brand brand--front">
      <div class="brand__name">TIDAL VERGE</div>
      <div class="brand__tagline">We'll take care of it.</div>
    </div>
  </section>

  <section class="card card--light card--back-bottom">
    <div class="brand brand--back">
      <div class="brand__name">TIDAL VERGE</div>
      <div class="brand__tagline">We'll take care of it.</div>
    </div>
    <div class="contact">
      <div class="contact__person">Darren Quellby</div>
      <div class="contact__line"><span class="contact__label">m:</span><span>0413562049</span></div>
      <div class="contact__line"><span class="contact__label">e:</span><span>norma.vance@fernmail.com.au</span></div>
      <div class="contact__cta">Call for free quote</div>
    </div>
  </section>

</main>
</body>
</html>
```